Business Card for TQB Field Services

Would like a large logo on one side. On the other side, logo on one side and company phone number, address, and email on the other side. I don't have a logo so please create one for us.
Updates
I don't have a logo, so please create one for us.
Target Market(s)
Land Surveying
Industry/Entity Type
Surveyor
Contact Information for Business Card
Would like a large logo on one side. On the other side, logo on one side and company phone number, address, and email on the other side
Requirements
Nice to have
- would like the initials to be incorporated with the logo

```html
<!DOCTYPE html>
<html lang="en">
<head>
<meta charset="utf-8">
<title>TQB Field Services – Business Card</title>
<link href="https://fonts.googleapis.com/css2?family=Open+Sans:wght@400;600;700&display=swap" rel="stylesheet">
<style>
  :root {
    --page-bg: #e8e5e0;
    --brand-green: #8dc63f;
    --brand-blue: #1ca8e3;
    --card-white: #ffffff;
    --text-grey: #555a5f;
    --icon-grey: #5c6166;
    --card-shadow: 0 14px 30px rgba(0,0,0,0.22);
  }
  * { margin: 0; padding: 0; box-sizing: border-box; }
  html, body {
    width: 1200px;
    height: 923px;
    overflow: hidden;
    background: var(--page-bg);
    font-family: "Open Sans", Arial, sans-serif;
  }
  .canvas {
    position: relative;
    width: 1200px;
    height: 923px;
  }
  .card {
    position: absolute;
    left: 300px;
    width: 600px;
    height: 343px;
    border-radius: 26px;
    box-shadow: var(--card-shadow);
  }
  .card-front {
    top: 80px;
    background: var(--brand-green);
    display: flex;
    align-items: center;
    justify-content: center;
  }
  .front-name {
    color: var(--card-white);
    font-weight: 700;
    font-size: 52px;
    letter-spacing: 0.5px;
  }
  .card-back {
    top: 500px;
    background: var(--card-white);
  }
  .back-name {
    position: absolute;
    left: 42px;
    top: 40px;
    color: var(--brand-blue);
    font-weight: 700;
    font-size: 26px;
  }
  .contact-block {
    position: absolute;
    left: 342px;
    top: 132px;
  }
  .person-name {
    color: var(--brand-blue);
    font-weight: 600;
    font-size: 20px;
    line-height: 1.2;
  }
  .person-role {
    color: var(--brand-green);
    font-size: 17px;
    line-height: 1.3;
    margin-bottom: 22px;
  }
  .contact-list { list-style: none; }
  .contact-item {
    display: flex;
    align-items: center;
    gap: 10px;
    color: var(--text-grey);
    font-size: 14.5px;
    height: 28px;
  }
  .contact-icon {
    width: 18px;
    height: 18px;
    flex: none;
    fill: none;
    stroke: var(--icon-grey);
    stroke-width: 1.4;
  }
</style>
</head>
<body>
<main class="canvas">
  <section class="card card-front">
    <p class="front-name">TQB Field Services</p>
  </section>

  <section class="card card-back">
    <p class="back-name">TQB Field Services</p>

    <div class="contact-block">
      <p class="person-name">Person’s Name</p>
      <p class="person-role">Designation</p>
      <ul class="contact-list">
        <li class="contact-item">
          <svg class="contact-icon" viewBox="0 0 18 18"><rect x="5" y="1.5" width="8" height="15" rx="1.5"/><line x1="8" y1="13.8" x2="10" y2="13.8"/></svg>
          555.014.2378
        </li>
        <li class="contact-item">
          <svg class="contact-icon" viewBox="0 0 18 18"><rect x="1.5" y="4" width="15" height="10"/><polyline points="1.5,4 9,10 16.5,4"/></svg>
          info@tqbfieldservices.com
        </li>
        <li class="contact-item">
          <svg class="contact-icon" viewBox="0 0 18 18"><circle cx="9" cy="9" r="7.5"/><ellipse cx="9" cy="9" rx="3.2" ry="7.5"/><line x1="1.5" y1="9" x2="16.5" y2="9"/><line x1="3" y1="5" x2="15" y2="5"/><line x1="3" y1="13" x2="15" y2="13"/></svg>
          tqbfieldservices.com
        </li>
        <li class="contact-item">
          <svg class="contact-icon" viewBox="0 0 18 18"><polygon points="2.5,3 16,9 2.5,15"/></svg>
          27, elm street, city, US
        </li>
      </ul>
    </div>
  </section>
</main>
</body>
</html>
```